Box Design for "harbors Pharmacy Probiotic"

We need an all around the box design for our our in house brand of probiotics.
The design must be ingenious but simple enough for people to understand.
Use of graphics/images is necessary but should not be the end all of the project.

The design must have our basic colors i.e blue/white/lime green

In the uploads you will find necessary information that needs to be placed on the back - if however you feel you have something better to say, go for it.

I have placed the old design - THATS NOT WHAT WE ARE LOOKING FOR. - the "Lark Pharmacy" in the light blue and lime green must however stay as it is our in-house brand

Leave a space somewhere on the back for a sticker that states things like expiry date/batch number etc.

Technical Stuff:
width:110mm
height:80mm
Depth:20mm

Break some eggs!
Updates

Target Market(s)

Everyone - more so, sick people.
People with Gastro Problems

Industry/Entity Type

Pharmacy

Colors
0255a3
85acd3
acd136
33a6d7

Requirements
Must have
• Logo
• "Lark Pharmacy" - Logo
• The Information on the back of the box stating whats in the box.
• Space for barcode
• Space for batch/expiry
• Design along in between the two planes - the depth
• It must have an out of the box approach to packaging in terms of design
Nice to have
• The blue highlight that goes around the logo.
Should not have
• No pictures of people -if there are pics of people, their eyes should not be visible - (religious thing)
• -Monotone.

```html
<!DOCTYPE html>
<html lang="en">
<head>
<meta charset="utf-8">
<title>Lark Pharmacy Probiotic – Box Artwork</title>
<link rel="stylesheet" href="https://fonts.googleapis.com/css2?family=Cinzel:wght@400;700&family=Open+Sans:wght@400;700;800&display=swap">
<style>
  :root {
    --white: #ffffff;
    --brand-blue: #0255a3;
    --deep-blue: #123f93;
    --mid-blue: #1f6fc4;
    --sky-blue: #33a6d7;
    --soft-blue: #85acd3;
    --lime: #c6d92c;
    --lime-dark: #acd136;
    --gold: #eccd45;
    --caption: #cfd9ee;
    --navy: #1b2a5c;
  }
  * { margin: 0; padding: 0; box-sizing: border-box; }
  html, body {
    width: 810px;
    height: 1200px;
    overflow: hidden;
    background: var(--white);
  }
  .canvas {
    position: relative;
    width: 810px;
    height: 1200px;
    background: var(--white);
    font-family: "Open Sans", Arial, sans-serif;
  }

  /* ---------- Front panel ---------- */
  .front-panel {
    position: absolute;
    left: 0; top: 0;
    width: 810px; height: 592px;
    overflow: hidden;
  }
  .front-panel .panel-shape {
    position: absolute; inset: 0;
    width: 810px; height: 592px;
  }
  .house-mark {
    position: absolute;
    top: 38px; left: 0; width: 810px;
    display: flex; justify-content: center; align-items: center; gap: 8px;
    font-family: "Open Sans", Arial, sans-serif;
    font-weight: 700;
    font-size: 16px;
    letter-spacing: 1px;
    text-transform: uppercase;
    color: var(--navy);
  }
  .house-mark .mark-square {
    width: 14px; height: 14px;
    background: var(--navy);
  }
  .brand-name {
    position: absolute;
    top: 100px; left: 0; width: 810px;
    text-align: center;
    font-family: "Open Sans", Arial, sans-serif;
    font-weight: 400;
    font-size: 56px;
    color: var(--sky-blue);
    letter-spacing: -0.5px;
  }
  .swirl-decor {
    position: absolute;
    border-radius: 50%;
    background: radial-gradient(closest-side, rgba(51,166,215,0.35), rgba(51,166,215,0));
  }
  .front-panel .swirl-decor.right { right: -60px; top: 200px; width: 300px; height: 380px; }
  .front-panel .swirl-decor.left { left: -80px; top: 380px; width: 260px; height: 240px; }
  .product-name {
    position: absolute;
    top: 360px; left: 0; width: 810px;
    text-align: center;
    font-family: "Cinzel", Georgia, serif;
    font-weight: 400;
    font-size: 58px;
    letter-spacing: 2px;
    color: var(--gold);
  }
  .product-detail {
    position: absolute;
    left: 0; width: 810px;
    text-align: center;
    font-family: "Cinzel", Georgia, serif;
    color: var(--caption);
  }
  .product-detail.strains { top: 470px; font-size: 30px; }
  .product-detail.count { top: 510px; font-size: 22px; letter-spacing: 1px; }

  /* ---------- Back panel ---------- */
  .back-panel {
    position: absolute;
    left: 0; top: 613px;
    width: 810px; height: 587px;
    overflow: hidden;
    background: linear-gradient(180deg, var(--mid-blue) 0%, var(--brand-blue) 45%, var(--deep-blue) 100%);
  }
  .back-panel .swirl-decor.left { left: -90px; top: 40px; width: 300px; height: 420px; }
  .back-panel .swirl-decor.right { right: -70px; top: -20px; width: 280px; height: 360px; }
  .product-info {
    position: absolute;
    top: 170px; left: 205px; width: 400px;
    text-align: center;
    font-family: "Open Sans", Arial, sans-serif;
    font-weight: 700;
    font-size: 12.5px;
    line-height: 16.5px;
    color: var(--gold);
  }
  .product-info p + p { margin-top: 16px; }
</style>
</head>
<body>
<div class="canvas">

  <section class="front-panel">
    <svg class="panel-shape" viewBox="0 0 810 592" xmlns="http://www.w3.org/2000/svg" aria-hidden="true">
      <defs>
        <linearGradient id="frontBlue" x1="0" y1="0" x2="0" y2="1">
          <stop offset="0" stop-color="#1f6fc4"/>
          <stop offset="0.5" stop-color="#0255a3"/>
          <stop offset="1" stop-color="#123f93"/>
        </linearGradient>
      </defs>
      <path d="M0,212 C180,250 360,235 520,180 C640,138 730,100 810,88 L810,592 L0,592 Z" fill="#c6d92c"/>
      <path d="M0,250 C200,262 380,240 540,190 C660,152 740,118 810,110 L810,592 L0,592 Z" fill="url(#frontBlue)"/>
    </svg>

    <div class="house-mark"><span class="mark-square"></span>harbors Pharmacy</div>
    <div class="brand-name">Lark Pharmacy</div>

    <div class="swirl-decor right" role="img" aria-label="Light blue flowing swirl ornament"></div>
    <div class="swirl-decor left" role="img" aria-label="Light blue flowing swirl ornament"></div>

    <h1 class="product-name">POBIOTIC</h1>
    <div class="product-detail strains">4 Stain</div>
    <div class="product-detail count">10 Caps</div>
  </section>

  <section class="back-panel">
    <div class="swirl-decor left" role="img" aria-label="Light blue flowing swirl ornament"></div>
    <div class="swirl-decor right" role="img" aria-label="Light blue flowing swirl ornament"></div>

    <div class="product-info">
      <p>Lorem ipsum dolor sit amet, consectetur adipiscing elit. Fusce dignissim pretium consectetur. Curabitur tempor posuere mauris in varius. Pellentesque viverra nibh eu vehicula mattis. Nullam porta facilisis justo, a feugiat dolor sodales sed. Vestibulum neque nisi, elementum tincidunt metus sit amet, egestas bibendum enim. Aenean a blandit elit, vel rutrum mi. Nunc dapibus turpis sed massa aliquet tincidunt.</p>
      <p>Pellentesque id neque ligula. Nullam posuere, ligula a mattis posuere, lacus nisl adipiscing nunc, eu congue justo est ut diam. Nam quam nibh, dignissim non consequat in, semper eget purus. Nulla arcu sapien, viverra vitae metus tempor, congue ornare diam.</p>
    </div>
  </section>

</div>
</body>
</html>
```